Editorial Website Design for High-End Custom Millwork Firm

Design (no development) for a 5-7 page website for a high-end custom architectural millwork firm. Editorial, magazine-quality aesthetic — think Dwelling Quarterly and top-tier millwork studios (Owen Tallard, Vorko). Full brief, reference sites, and project photography attached. We have uploaded a sample of our photography to use in your design. PLEASE READ PDF DOCUMENT BRIEF!!!

```html
<!DOCTYPE html>
<html lang="en">
<head>
<meta charset="utf-8">
<title>Larkspur Joinery — Website Design Board</title>
<link href="https://fonts.googleapis.com/css2?family=Newsreader:ital,opsz,wght@0,6..72,300;0,6..72,400;1,6..72,300&family=Inter:wght@400;500;600&display=swap" rel="stylesheet">
<style>
:root{
  --board:#a9a9a9;
  --ivory:#faf6f1;
  --ivory-2:#f7f2ea;
  --ivory-3:#efe7dc;
  --sand:#ecdccd;
  --oak:#9b7351;
  --walnut:#6b4a32;
  --ebony:#24170f;
  --brass-pale:#fbf4eb;
  --brass-light:#cfa75f;
  --brass:#a47a43;
  --brass-dark:#2d2013;
  --n1:#faf9f7;--n2:#d8cdbe;--n3:#6f6a61;--ink:#1f1e1b;
  --e1:#fff2ef;--e2:#c85d4f;--e3:#a94438;
  --s1:#f3f7ef;--s2:#789653;--s3:#5f7d3d;
  --footer:#2d241d;
  --dark:#2a221d;
  --rule:#e4d9c9;
  --serif:'Newsreader',Georgia,serif;
  --sans:'Inter',Arial,sans-serif;
}
*{box-sizing:border-box;margin:0;padding:0}
html,body{width:1200px;height:1200px;overflow:hidden;background:var(--board)}
.stage{position:absolute;left:0;top:0;width:1932px;height:1932px;transform:scale(.62112);transform-origin:0 0;background:var(--board);font-family:var(--sans);color:var(--ink)}
.abs{position:absolute}
.page{position:absolute;width:450px;background:var(--ivory);overflow:hidden}
.page--home{left:369px;top:55px;height:1251px}
.page--cont{left:866px;top:0;height:1557px}
.photo{position:absolute}
.ph-kitchen{background:linear-gradient(160deg,#f4efe6,#e2d7c6 55%,#a98560)}
.ph-commercial{background:linear-gradient(135deg,#4a3325,#8b6248 50%,#4f6b38)}
.ph-shop{background:linear-gradient(150deg,#6f6a61,#b9b0a0 50%,#7a6a55)}
.ph-drawer{background:linear-gradient(180deg,#c9c4bd,#a9a39c 40%,#c58f55 60%,#b8b2ab)}
.ph-sanding{background:linear-gradient(140deg,#d9dadb,#5f7590 55%,#cfc8bd)}
.ph-assembly{background:linear-gradient(140deg,#3a332d,#c49a6c 60%,#e6d4b8)}
.ph-swatch-oak{background:linear-gradient(135deg,#c48a4c,#8e5d31)}
.ph-swatch-fluted{background:linear-gradient(90deg,#dcc9a8,#c8ad82)}
.ph-swatch-cane{background:linear-gradient(135deg,#b98b58,#7c5634)}
.arch{position:absolute;background:#c9a77b;border-radius:60px 60px 0 0}
.eyebrow{position:absolute;font-size:4px;letter-spacing:.18em;text-transform:uppercase;color:var(--brass);font-weight:600;white-space:nowrap}
.serif{font-family:var(--serif);font-weight:300;color:#2a2520}
.tiny{font-size:4px;color:#5a524a;line-height:1.5}
.small{font-size:5px;color:#3a342e;line-height:1.6}
.caption{position:absolute;font-size:4px;color:#6a6056;white-space:nowrap}
.caption--italic{font-family:var(--serif);font-style:italic;font-size:5px}
.section-rule{position:absolute;left:0;width:450px;height:1px;background:var(--rule)}
.nav{position:absolute;left:0;top:0;width:450px;height:30px}
.wordmark{position:absolute;font-family:var(--sans);font-weight:500;font-size:7px;color:#2a2520;white-space:nowrap}
.nav-links{position:absolute;left:246px;top:12px;display:flex;gap:14px;font-size:3.5px;color:#4a423b}
.btn-solid{position:absolute;background:var(--walnut);color:#fff;font-size:3.5px;display:flex;align-items:center;justify-content:center;white-space:nowrap}
.hero{position:absolute;left:0;top:0;width:450px;height:225px;background:var(--ivory-2)}
.band{position:absolute;left:0;width:450px;height:28px;background:var(--ivory-2);border-top:1px solid var(--rule);border-bottom:1px solid var(--rule);display:flex;align-items:center;gap:9px;padding-left:16px;font-size:3.2px;letter-spacing:.12em;text-transform:uppercase;color:#3a342e;white-space:nowrap}
.band .gap{width:16px;height:8px;border-left:1px solid var(--rule)}
.fact-list{position:absolute;width:99px}
.fact-list div{font-size:4.5px;color:#3a342e;height:22px;padding-top:2px;border-bottom:1px solid #d8c9b4;white-space:nowrap}
.quote{position:absolute;font-family:var(--serif);font-weight:300;font-size:13px;line-height:1.42;color:#2a2520}
.quote-mark{position:absolute;width:18px;height:1px;background:var(--brass-light)}
.h2{position:absolute;font-family:var(--serif);font-weight:300;color:#2a2520;white-space:nowrap}
.index{position:absolute;font-size:3.6px;color:#8a7f73;display:flex;gap:8px;white-space:nowrap}
.build-list{position:absolute;width:256px}
.build-row{position:relative;height:24.5px;border-bottom:1px solid var(--rule);display:flex;align-items:center;font-size:5.5px;color:#3a342e}
.build-row b{font-weight:400;color:var(--brass);width:26px;padding-left:7px}
.build-thumb{position:absolute;right:0;top:3px;height:19px}
.steps{position:absolute;width:60px}
.step{height:39px;border-bottom:1px solid var(--rule);padding-top:2px}
.step b{display:block;font-family:var(--serif);font-weight:300;font-size:10px;color:var(--brass)}
.step span{font-size:4px;color:#3a342e}
.dark{position:absolute;left:0;top:1051px;width:450px;height:276px;background:var(--dark);color:#e9dfd1}
.dark .eyebrow{color:#b89563}
.stats{position:absolute;left:26px;top:224px;width:400px;height:32px;display:flex}
.stats div{flex:1;display:flex;align-items:center;justify-content:center;text-align:center;font-size:4px;letter-spacing:.2em;color:#d8cbb8;border-right:1px solid #4a3f36;line-height:1.6}
.stats div:last-child{border-right:0}
.cta-box{position:absolute;left:303px;top:1346px;width:118px;height:100px;border:1px solid #d5c2a6;background:var(--ivory)}
.footer{position:absolute;left:0;top:1460px;width:450px;height:97px;background:var(--ivory-3)}
.foot-col{position:absolute;top:16px;font-size:3.6px;color:#4a423b;line-height:2.5;white-space:nowrap}
.foot-col .eyebrow{position:static;display:block;font-size:3.4px;line-height:1}
.library{position:absolute;left:37px;top:1590px;width:1855px;height:240px;background:#f5f3ef}
.library-title{position:absolute;left:31px;top:10px;font-family:var(--serif);font-weight:400;font-size:27px;color:#2a2520}
.group{position:absolute;top:46px;height:102px;border:1px solid #d9d4cc;background:#f8f6f2}
.group h4{position:absolute;left:10px;top:4px;font-size:11px;font-weight:500;letter-spacing:.02em;color:#2a2520}
.group h5{position:absolute;left:10px;top:19px;font-size:11px;font-weight:400;color:#5a524a}
.chip{position:absolute;top:38px;height:38px;border:1px solid #ddd6cc}
.chip-label{position:absolute;top:81px;font-size:11px;color:#3a342e;text-align:center}
.core{position:absolute;left:20px;top:160px;width:1813px;height:72px;border:1px solid #d9d4cc;background:#f8f6f2}
.core h4{position:absolute;left:14px;top:10px;font-size:12px;font-weight:500;color:#2a2520}
.core-bar{position:absolute;top:7px;height:29px}
.core-label{position:absolute;top:40px;font-size:11px;color:#3a342e;text-align:center;line-height:1.3}
</style>
</head>
<body>
<div class="stage">

<section class="page page--home">
  <div class="hero"></div>
  <header class="nav">
    <div class="wordmark" style="left:11px;top:10px">Larkspur Joinery</div>
    <nav class="nav-links"><span>Projects</span><span>Services</span><span>Capabilities</span><span>About</span><span>Blog</span><span>Contact</span></nav>
    <div class="btn-solid" style="left:398px;top:9px;width:38px;height:11px">Start a Project</div>
  </header>

  <div class="eyebrow" style="left:16px;top:52px;font-size:3.4px">Millbrook, OR · Est. 1994 · GMA Quality Premium Grade</div>
  <h1 class="h2" style="left:16px;top:63px;font-size:20px;line-height:21.5px">Architectural Millwork,<br>Crafted <i>for</i><br>Exceptional Interiors</h1>
  <p class="abs small" style="left:17px;top:136px;width:110px;font-size:4.6px">Custom architectural millwork and cabinetry for commercial interiors, luxury residences, architects, and designers.</p>
  <div class="btn-solid" style="left:17px;top:166px;width:46px;height:13px">View Projects</div>
  <div class="abs" style="left:71px;top:169px;font-size:4px;color:#3a342e;white-space:nowrap">Start a Conversation ⟶</div>

  <div class="arch" style="left:206px;top:28px;width:80px;height:104px"></div>
  <div class="photo ph-commercial" style="left:206px;top:65px;width:80px;height:70px" role="img" aria-label="Commercial lobby with walnut reception desk and patterned screen"></div>
  <div class="photo ph-kitchen" style="left:281px;top:28px;width:120px;height:132px" role="img" aria-label="Bright kitchen with white cabinetry and oak island"></div>
  <div class="photo ph-shop" style="left:184px;top:120px;width:102px;height:65px" role="img" aria-label="Craftsman assembling a lattice panel in the shop"></div>
  <div class="photo ph-drawer" style="left:286px;top:135px;width:85px;height:68px" role="img" aria-label="Painted drawer fronts with oak inset pulls"></div>
  <div class="photo ph-swatch-oak" style="left:184px;top:190px;width:32px;height:20px" role="img" aria-label="White oak sample"></div>
  <div class="photo ph-swatch-fluted" style="left:219px;top:190px;width:32px;height:20px" role="img" aria-label="Fluted cabinetry sample"></div>
  <div class="photo ph-swatch-cane" style="left:253px;top:190px;width:32px;height:20px" role="img" aria-label="Cane detail sample"></div>
  <div class="caption" style="left:192px;top:214px;font-size:3px">White Oak</div>
  <div class="caption" style="left:222px;top:214px;font-size:3px">Fluted Cabinetry</div>
  <div class="caption" style="left:262px;top:214px;font-size:3px">Cane Detail</div>
  <div class="caption" style="left:414px;top:73px;font-size:3.2px">Custom<br>Cabinetry</div>
  <div class="caption" style="left:414px;top:126px;font-size:3.2px">Hand-finished<br>Grade</div>
  <div class="caption" style="left:388px;top:173px;font-size:3.2px">Built in<br>Millbrook</div>
  <div class="caption" style="left:173px;top:103px;font-size:3.2px">Architectural<br>Woodwork</div>
  <svg class="abs" style="left:170px;top:60px" width="250" height="130" fill="none" stroke="#8a7a66" stroke-width=".4">
    <path d="M232 15 H222"/><path d="M232 68 H222"/><path d="M206 116 H190"/><path d="M28 45 H12"/>
  </svg>

  <div class="band" style="top:225px"><span>Architectural Millwork</span>/<span>Custom Cabinetry</span>/<span>Commercial Interiors</span>/<span>Residential Built-ins</span><span class="gap"></span><span>Family Owned</span><span>Premium Grade</span><span>Built to Spec</span></div>

  <p class="quote" style="left:21px;top:311px;width:125px">“Since 1994, Larkspur Joinery has shaped interiors where craftsmanship is meant to be seen.”</p>
  <div class="quote-mark" style="left:25px;top:414px"></div>
  <div class="photo ph-shop" style="left:154px;top:290px;width:150px;height:133px" role="img" aria-label="Craftsman measuring a lattice frame at the workbench"></div>
  <div class="fact-list" style="left:330px;top:318px"><div>Millbrook, Oregon</div><div>Established 1994</div><div>GMA Quality Premium Grade</div><div>60% Commercial / 40% Residential</div></div>

  <div class="section-rule" style="top:472px"></div>
  <div class="eyebrow" style="left:14px;top:485px">Selected Work</div>
  <h2 class="h2" style="left:14px;top:497px;font-size:14px;line-height:18px">Commercial interiors, private residences,<br>and custom architectural details built with precision.</h2>
  <div class="photo ph-kitchen" style="left:14px;top:543px;width:245px;height:179px" role="img" aria-label="Residential kitchen with oak island and white cabinetry"></div>
  <div class="photo ph-commercial" style="left:266px;top:543px;width:169px;height:86px" role="img" aria-label="Commercial reception with walnut desk"></div>
  <div class="photo ph-drawer" style="left:266px;top:645px;width:169px;height:77px" role="img" aria-label="Custom drawer fronts with oak inlays"></div>
  <div class="caption" style="left:14px;top:726px">Residential Cabinetry</div>
  <div class="caption" style="left:266px;top:632px">Commercial Interiors</div>
  <div class="caption" style="left:266px;top:726px">Custom Architectural Details</div>
  <div class="section-rule" style="left:14px;top:748px;width:420px"></div>
  <div class="index" style="left:14px;top:754px"><span>01 Residential Cabinetry</span>/<span>02 Commercial Interiors</span>/<span>03 Custom Details</span>/<span>04 Built-in Millwork</span></div>

  <div class="section-rule" style="top:773px"></div>
  <div class="eyebrow" style="left:19px;top:811px;color:#6a6056">Capabilities</div>
  <h2 class="h2" style="left:19px;top:828px;font-size:19px">What We Build</h2>
  <p class="abs tiny" style="left:19px;top:859px;width:110px">From commercial interiors to finely detailed residential cabinetry, Larkspur Joinery carries projects from shop drawings through fabrication and installation.</p>
  <div class="build-list" style="left:178px;top:803px">
    <div class="build-row"><b>01</b>Architectural Millwork</div>
    <div class="build-row"><b>02</b>Custom Cabinetry<div class="photo ph-drawer build-thumb" style="width:62px" role="img" aria-label="Cabinetry detail"></div></div>
    <div class="build-row"><b>03</b>Commercial Interiors<div class="photo ph-commercial build-thumb" style="width:120px" role="img" aria-label="Commercial interior"></div></div>
    <div class="build-row"><b>04</b>Residential Built-ins<div class="photo ph-kitchen build-thumb" style="width:62px" role="img" aria-label="Residential built-in"></div></div>
    <div class="build-row"><b>05</b>Specialty Details</div>
    <div class="build-row"><b>06</b>Fabrication + Installation</div>
  </div>
  <div class="abs" style="left:178px;top:960px;font-size:3.4px;color:#6a6056;white-space:nowrap">Designed, fabricated, finished, and installed with premium-grade standards.</div>

  <div class="section-rule" style="top:985px"></div>
  <div class="eyebrow" style="left:19px;top:999px">Craft + Process</div>
  <h2 class="h2" style="left:19px;top:1014px;font-size:19px;line-height:21px;font-weight:400">Built by Hand,<br>Refined by Process</h2>
  <p class="abs tiny" style="left:19px;top:1061px;width:176px">Every project moves through a disciplined path: design review, engineering, fabrication, finishing, and installation. The work is measured, built, and checked by craftspeople before it reaches the room.</p>
  <div class="photo ph-shop" style="left:16px;top:1095px;width:199px;height:138px" role="img" aria-label="Shop fabrication of a lattice panel"></div>
  <div class="photo ph-sanding" style="left:221px;top:1053px;width:123px;height:78px" role="img" aria-label="Craftsman shaping material with a sander"></div>
  <div class="photo ph-assembly" style="left:221px;top:1147px;width:123px;height:86px" role="img" aria-label="Assembly of a curved wood frame"></div>
  <div class="caption caption--italic" style="left:16px;top:1235px">Shop fabrication</div>
  <div class="caption caption--italic" style="left:221px;top:1133px">Material shaping</div>
  <div class="caption caption--italic" style="left:221px;top:1235px">Assembly detail</div>
  <div class="steps" style="left:368px;top:1055px">
    <div class="step"><b>01</b><span>Design Review</span></div>
    <div class="step"><b>02</b><span>Engineering</span></div>
    <div class="step"><b>03</b><span>Fabrication</span></div>
    <div class="step"><b>04</b><span>Finishing</span></div>
    <div class="step" style="border:0"><b>05</b><span>Installation</span></div>
  </div>
</section>

<section class="page page--cont">
  <div class="abs" style="left:0;top:0;width:450px;height:20px;background:var(--ivory-2)"></div>
  <div class="photo ph-swatch-oak" style="left:184px;top:0;width:35px;height:8px" role="img" aria-label="White oak sample"></div>
  <div class="photo ph-swatch-fluted" style="left:222px;top:0;width:30px;height:8px" role="img" aria-label="Fluted cabinetry sample"></div>
  <div class="photo ph-swatch-cane" style="left:256px;top:0;width:30px;height:8px" role="img" aria-label="Cane detail sample"></div>
  <div class="caption" style="left:192px;top:11px;font-size:3px">White Oak</div>
  <div class="caption" style="left:222px;top:11px;font-size:3px">Fluted Cabinetry</div>
  <div class="caption" style="left:262px;top:11px;font-size:3px">Cane Detail</div>
  <div class="band" style="top:20px"><span>Architectural Millwork</span>/<span>Custom Cabinetry</span>/<span>Commercial Interiors</span>/<span>Residential Built-ins</span><span class="gap"></span><span>Family Owned</span><span>Premium Grade</span><span>Built to Spec</span></div>

  <p class="quote" style="left:22px;top:106px;width:125px">“Since 1994, Larkspur Joinery has shaped interiors where craftsmanship is meant to be seen.”</p>
  <div class="quote-mark" style="left:26px;top:210px"></div>
  <div class="photo ph-shop" style="left:155px;top:85px;width:150px;height:134px" role="img" aria-label="Craftsman measuring a lattice frame at the workbench"></div>
  <div class="fact-list" style="left:331px;top:113px"><div>Millbrook, Oregon</div><div>Established 1994</div><div>GMA Quality Premium Grade</div><div>60% Commercial / 40% Residential</div></div>

  <div class="section-rule" style="top:268px"></div>
  <div class="eyebrow" style="left:14px;top:280px">Selected Work</div>
  <h2 class="h2" style="left:14px;top:292px;font-size:14px;line-height:18px">Commercial interiors, private residences,<br>and custom architectural details built with precision.</h2>
  <div class="photo ph-kitchen" style="left:14px;top:339px;width:245px;height:179px" role="img" aria-label="Residential kitchen with oak island and white cabinetry"></div>
  <div class="photo ph-commercial" style="left:266px;top:339px;width:170px;height:86px" role="img" aria-label="Commercial reception with walnut desk"></div>
  <div class="photo ph-drawer" style="left:266px;top:441px;width:170px;height:77px" role="img" aria-label="Custom drawer fronts with oak inlays"></div>
  <div class="caption" style="left:14px;top:522px">Residential Cabinetry</div>
  <div class="caption" style="left:266px;top:428px">Commercial Interiors</div>
  <div class="caption" style="left:266px;top:522px">Custom Architectural Details</div>
  <div class="section-rule" style="left:14px;top:543px;width:420px"></div>
  <div class="index" style="left:14px;top:550px"><span>01 Residential Cabinetry</span>/<span>02 Commercial Interiors</span>/<span>03 Custom Details</span>/<span>04 Built-in Millwork</span></div>

  <div class="eyebrow" style="left:19px;top:606px;color:#6a6056">Capabilities</div>
  <h2 class="h2" style="left:19px;top:623px;font-size:19px">What We Build</h2>
  <p class="abs tiny" style="left:19px;top:655px;width:110px">From commercial interiors to finely detailed residential cabinetry, Larkspur Joinery carries projects from shop drawings through fabrication and installation.</p>
  <div class="build-list" style="left:178px;top:599px">
    <div class="build-row"><b>01</b>Architectural Millwork</div>
    <div class="build-row"><b>02</b>Custom Cabinetry<div class="photo ph-drawer build-thumb" style="width:62px" role="img" aria-label="Cabinetry detail"></div></div>
    <div class="build-row"><b>03</b>Commercial Interiors<div class="photo ph-commercial build-thumb" style="width:120px" role="img" aria-label="Commercial interior"></div></div>
    <div class="build-row"><b>04</b>Residential Built-ins<div class="photo ph-kitchen build-thumb" style="width:62px" role="img" aria-label="Residential built-in"></div></div>
    <div class="build-row"><b>05</b>Specialty Details</div>
    <div class="build-row"><b>06</b>Fabrication + Installation</div>
  </div>
  <div class="abs" style="left:178px;top:757px;font-size:3.4px;color:#6a6056;white-space:nowrap">Designed, fabricated, finished, and installed with premium-grade standards.</div>

  <div class="section-rule" style="top:783px"></div>
  <div class="eyebrow" style="left:20px;top:795px">Craft + Process</div>
  <div class="abs" style="left:20px;top:803px;width:28px;height:1px;background:var(--brass-light)"></div>
  <h2 class="h2" style="left:20px;top:809px;font-size:19px;line-height:21px;font-weight:400">Built by Hand,<br>Refined by Process</h2>
  <p class="abs tiny" style="left:20px;top:856px;width:176px">Every project moves through a disciplined path: design review, engineering, fabrication, finishing, and installation. The work is measured, built, and checked by craftspeople before it reaches the room.</p>
  <div class="photo ph-shop" style="left:16px;top:890px;width:199px;height:138px" role="img" aria-label="Shop fabrication of a lattice panel"></div>
  <div class="photo ph-sanding" style="left:222px;top:849px;width:122px;height:77px" role="img" aria-label="Craftsman shaping material with a sander"></div>
  <div class="photo ph-assembly" style="left:222px;top:943px;width:122px;height:85px" role="img" aria-label="Assembly of a curved wood frame"></div>
  <div class="caption caption--italic" style="left:16px;top:1031px">Shop fabrication</div>
  <div class="caption caption--italic" style="left:222px;top:928px">Material shaping</div>
  <div class="caption caption--italic" style="left:222px;top:1031px">Assembly detail</div>
  <div class="steps" style="left:368px;top:851px">
    <div class="step"><b>01</b><span>Design Review</span></div>
    <div class="step"><b>02</b><span>Engineering</span></div>
    <div class="step"><b>03</b><span>Fabrication</span></div>
    <div class="step"><b>04</b><span>Finishing</span></div>
    <div class="step" style="border:0"><b>05</b><span>Installation</span></div>
  </div>

  <div class="dark">
    <div class="eyebrow" style="left:26px;top:26px">Quality + Legacy</div>
    <div class="abs" style="left:92px;top:28px;width:30px;height:1px;background:#6a5540"></div>
    <h2 class="h2" style="left:26px;top:49px;font-size:29px;line-height:31px;color:#efe6d8">Quality is built<br>into the process.</h2>
    <p class="abs" style="left:26px;top:124px;font-family:var(--serif);font-weight:300;font-size:8px;color:#c9a46a;white-space:nowrap">Premium-grade work, measured at every stage.</p>
    <p class="abs" style="left:26px;top:143px;width:135px;font-size:5px;line-height:1.6;color:#d8cbb8">Larkspur Joinery brings certified standards, experienced craftspeople, and careful project coordination to commercial and residential interiors.</p>
    <div class="abs" style="left:222px;top:0;width:1px;height:205px;background:#4a3f36"></div>
    <div class="photo ph-shop" style="left:245px;top:17px;width:128px;height:187px;outline:1.5px solid #a47a43;outline-offset:-2px" role="img" aria-label="Craftsman building a lattice panel"></div>
    <div class="abs" style="left:384px;top:143px;font-size:3.4px;letter-spacing:.2em;color:#a89580;line-height:3.7;white-space:nowrap">MILLBROOK, OR<br>ESTABLISHED 1994<br>CERTIFIED<br>STANDARDS</div>
    <div class="abs" style="left:26px;top:212px;width:400px;height:1px;background:#4a3f36"></div>
    <div class="stats"><div>GMA QUALITY<br>PREMIUM GRADE</div><div>MWB<br>CERTIFICATION</div><div>ESTABLISHED<br>1994</div><div>BUILT IN<br>MILLBROOK, OR</div></div>
  </div>

  <div class="eyebrow" style="left:30px;top:1350px">Start a Project</div>
  <div class="abs" style="left:84px;top:1352px;width:28px;height:1px;background:var(--brass-light)"></div>
  <h2 class="h2" style="left:30px;top:1366px;font-size:22px;line-height:27px">Have a project<br>that demands<br>careful execution?</h2>
  <svg class="abs" style="left:170px;top:1395px" width="135" height="25" fill="none" stroke="#c9a46a" stroke-width=".7"><path d="M0 22 H88 C100 22 102 2 120 2 H135"/></svg>
  <div class="cta-box">
    <p class="abs tiny" style="left:14px;top:13px;width:90px;font-size:4.2px">Tell us about the room, the schedule, and the level of finish required.</p>
    <div class="abs" style="left:14px;top:49px;width:28px;height:1px;background:var(--brass-light)"></div>
    <div class="abs" style="left:14px;top:60px;font-family:var(--serif);font-size:10px;color:var(--brass);white-space:nowrap">Start a Project <span style="font-family:var(--sans);font-size:8px">⟶</span></div>
    <div class="abs" style="left:14px;top:84px;font-size:2.9px;letter-spacing:.12em;color:#4a423b;white-space:nowrap">COMMERCIAL + RESIDENTIAL / MILLBROOK, OR</div>
  </div>

  <footer class="footer">
    <div class="wordmark" style="left:29px;top:15px;font-size:10px">Larkspur Joinery</div>
    <div class="abs" style="left:29px;top:38px;font-size:3.4px;letter-spacing:.2em;color:#3a342e;line-height:2.4;white-space:nowrap">MILLBROOK, OREGON<br>ESTABLISHED 1994</div>
    <div class="abs" style="left:157px;top:12px;width:1px;height:60px;background:var(--rule)"></div>
    <div class="foot-col" style="left:175px"><span class="eyebrow">Explore</span>Projects<br>Services<br>About<br>Blog<br>Contact</div>
    <div class="abs" style="left:231px;top:12px;width:1px;height:60px;background:var(--rule)"></div>
    <div class="foot-col" style="left:249px"><span class="eyebrow">Capabilities</span>Architectural Millwork<br>Custom Cabinetry<br>Commercial Interiors<br>Residential Built-ins</div>
    <div class="abs" style="left:320px;top:12px;width:1px;height:60px;background:var(--rule)"></div>
    <div class="foot-col" style="left:339px"><span class="eyebrow">Credentials</span>GMA Quality Premium Grade<br>MWB Certified<br>Commercial + Residential</div>
    <div class="abs" style="left:29px;top:82px;width:392px;height:1px;background:var(--rule)"></div>
    <div class="abs" style="left:29px;top:86px;font-size:3.4px;color:#4a423b;white-space:nowrap">© 2026 Larkspur Joinery. All rights reserved.</div>
    <div class="abs" style="left:350px;top:86px;font-size:3.4px;color:#4a423b;white-space:nowrap">studio@larkspurjoinery.com</div>
  </footer>
</section>

<section class="library">
  <h3 class="library-title">Color Library</h3>

  <div class="group" style="left:23px;width:295px"><h4>PRIMARY</h4><h5>Warm Ivory</h5>
    <div class="chip" style="left:8px;width:80px;background:var(--ivory)"></div>
    <div class="chip" style="left:99px;width:80px;background:var(--ivory-2)"></div>
    <div class="chip" style="left:190px;width:90px;background:var(--ivory-3)"></div>
    <div class="chip-label" style="left:8px;width:80px">#FAF6F1</div><div class="chip-label" style="left:99px;width:80px">#F7F2EA</div><div class="chip-label" style="left:190px;width:90px">#EFE7DC</div>
  </div>
  <div class="group" style="left:338px;width:344px"><h4>SECONDARY</h4><h5>Walnut / Wood</h5>
    <div class="chip" style="left:8px;width:70px;background:var(--sand)"></div>
    <div class="chip" style="left:91px;width:70px;background:var(--oak)"></div>
    <div class="chip" style="left:174px;width:70px;background:var(--walnut)"></div>
    <div class="chip" style="left:256px;width:65px;background:var(--ebony)"></div>
    <div class="chip-label" style="left:8px;width:70px">#ECDCCD</div><div class="chip-label" style="left:91px;width:70px">#9B7351</div><div class="chip-label" style="left:174px;width:70px">#6B4A32</div><div class="chip-label" style="left:256px;width:65px">#24170F</div>
  </div>
  <div class="group" style="left:710px;width:327px"><h4>ACCENT</h4><h5>Aged Brass</h5>
    <div class="chip" style="left:8px;width:70px;background:var(--brass-pale)"></div>
    <div class="chip" style="left:92px;width:66px;background:var(--brass-light)"></div>
    <div class="chip" style="left:172px;width:66px;background:var(--brass)"></div>
    <div class="chip" style="left:251px;width:62px;background:var(--brass-dark)"></div>
    <div class="chip-label" style="left:8px;width:70px">#FBF4EB</div><div class="chip-label" style="left:92px;width:66px">#CFA75F</div><div class="chip-label" style="left:172px;width:66px">#A47A43</div><div class="chip-label" style="left:251px;width:62px">#2D2013</div>
  </div>
  <div class="group" style="left:1050px;width:288px"><h4>NEUTRAL</h4><h5>Editorial Charcoal</h5>
    <div class="chip" style="left:8px;width:58px;background:var(--n1)"></div>
    <div class="chip" style="left:78px;width:58px;background:var(--n2)"></div>
    <div class="chip" style="left:149px;width:58px;background:var(--n3)"></div>
    <div class="chip" style="left:219px;width:58px;background:var(--ink)"></div>
    <div class="chip-label" style="left:8px;width:58px">#FAF9F7</div><div class="chip-label" style="left:78px;width:58px">#D8CDBE</div><div class="chip-label" style="left:149px;width:58px">#6F6A61</div><div class="chip-label" style="left:219px;width:58px">#1F1E1B</div>
  </div>
  <div class="group" style="left:1365px;width:211px"><h4>ERROR</h4><h5>Muted Clay Red</h5>
    <div class="chip" style="left:8px;width:56px;background:var(--e1)"></div>
    <div class="chip" style="left:76px;width:56px;background:var(--e2)"></div>
    <div class="chip" style="left:145px;width:56px;background:var(--e3)"></div>
    <div class="chip-label" style="left:8px;width:56px">#FFF2EF</div><div class="chip-label" style="left:76px;width:56px">#C85D4F</div><div class="chip-label" style="left:145px;width:56px">#A94438</div>
  </div>
  <div class="group" style="left:1609px;width:224px"><h4>SUCCESS</h4><h5>Deep Olive</h5>
    <div class="chip" style="left:10px;width:58px;background:var(--s1)"></div>
    <div class="chip" style="left:85px;width:58px;background:var(--s2)"></div>
    <div class="chip" style="left:155px;width:58px;background:var(--s3)"></div>
    <div class="chip-label" style="left:10px;width:58px">#F3F7EF</div><div class="chip-label" style="left:85px;width:58px">#789653</div><div class="chip-label" style="left:155px;width:58px">#5F7D3D</div>
  </div>

  <div class="core"><h4>CORE USAGE</h4>
    <div class="core-bar" style="left:193px;width:258px;background:var(--ivory);border:1px solid #ddd6cc"></div>
    <div class="core-bar" style="left:522px;width:235px;background:var(--ink)"></div>
    <div class="core-bar" style="left:846px;width:229px;background:var(--walnut)"></div>
    <div class="core-bar" style="left:1163px;width:225px;background:var(--brass)"></div>
    <div class="core-bar" style="left:1485px;width:225px;background:var(--footer)"></div>
    <div class="core-label" style="left:193px;width:258px">Background<br>#FAF6F1</div>
    <div class="core-label" style="left:522px;width:235px">Text<br>#1F1E1B</div>
    <div class="core-label" style="left:846px;width:229px">Wood<br>#6B4A32</div>
    <div class="core-label" style="left:1163px;width:225px">Accent<br>#A47A43</div>
    <div class="core-label" style="left:1485px;width:225px">Footer<br>#2D241D</div>
  </div>
</section>

</div>
</body>
</html>
```